Etiketten für eine Apotherflasche
Zielgruppe
Wir sind eine Familienbrennerei aus Karlsruhe-Bulach, die von Vater und Tochter geführt wird. Wir stellen Edeldestillate, Whiskys, Gins und Liköre in Handarbeit her und legen großen Wert auf die Verwendung regionaler Rohstoffe, hauptsächlich von unseren eigenen Streuobstwiesen.
Aufgabenstellung
Wir benötigen ein Flaschenetikett für eine klassische Apotherflasche 0,5 Liter.
Der Inhalt wird unser 'Feldmarer Gin' sein.
Das Etikett sollte auf jeden Fall den Produktnamen 'Feldmarer Gin' enthalten.
Es wäre schön, wenn das Desgin die Stadt Karlsruhe wiederspiegeln würde - z.B. Fächer (da Fächerstadt), Stadtkarte im Hintergrund, Pyramide (Wahrzeichen von Karlsruhe) - hier dürfen Sie gerne kreativ werden.
Informationen zu uns bzw. unserer Brennerei finden Sie unter www.valdenhof-brennerei.de.
Bitte nicht an den dort existierenden Etiketten orientieren - diese werden akteuell umgestellt.
Maße des Etiketts sollten ca. 95x85mm sein.
Wir freuen uns auf die

```html
<!DOCTYPE html>
<html lang="de">
<head>
<meta charset="utf-8">
<title>Feldmarer Gin – Flaschenetikett</title>
<link rel="stylesheet" href="https://fonts.googleapis.com/css2?family=Oswald:wght@400;500;600&family=Pinyon+Script&display=swap">
<style>
  :root {
    --backdrop-top: #535a64;
    --backdrop-bottom: #30343a;
    --label-paper: #f1f3f1;
    --label-paper-shade: #e6eae8;
    --ink-green: #1f4d2c;
    --ink-dark: #2a2d2b;
    --frame-line: #3a3d3b;
    --skyline-light: #dde3e0;
    --skyline-deep: #c3cbc7;
  }
  * { margin: 0; padding: 0; box-sizing: border-box; }
  html, body {
    width: 1200px;
    height: 1200px;
    overflow: hidden;
  }
  body {
    background: linear-gradient(180deg, var(--backdrop-top), var(--backdrop-bottom));
    position: relative;
  }
  .label {
    position: absolute;
    left: 270px;
    top: 217px;
    width: 660px;
    height: 766px;
    background: linear-gradient(180deg, var(--label-paper), var(--label-paper-shade));
  }
  .label-frame {
    position: absolute;
    left: 38px;
    top: 38px;
    width: 584px;
    height: 654px;
    border: 2px solid var(--frame-line);
  }
  .distillery-name {
    position: absolute;
    top: 68px;
    left: 0;
    width: 100%;
    display: flex;
    justify-content: center;
    gap: 62px;
    font-family: "Oswald", sans-serif;
    font-weight: 500;
    font-size: 23px;
    letter-spacing: 2px;
    color: var(--ink-dark);
  }
  .product-name {
    position: absolute;
    top: 112px;
    left: 0;
    width: 100%;
    text-align: center;
    font-family: "Oswald", sans-serif;
    font-weight: 500;
    font-size: 100px;
    line-height: 1;
    letter-spacing: 4px;
    color: var(--ink-green);
  }
  .story {
    position: absolute;
    top: 236px;
    left: 40px;
    width: 580px;
    text-align: center;
    font-family: "Pinyon Script", cursive;
    font-size: 21px;
    line-height: 30px;
    letter-spacing: 2.2px;
    color: var(--ink-dark);
  }
  .product-type {
    position: absolute;
    top: 350px;
    left: 0;
    width: 100%;
    text-align: center;
    font-family: "Oswald", sans-serif;
    font-weight: 600;
    font-size: 86px;
    line-height: 1;
    letter-spacing: 3px;
    color: var(--ink-green);
  }
  .product-type-rule {
    position: absolute;
    top: 452px;
    left: 258px;
    width: 150px;
    height: 3px;
    background: var(--ink-dark);
  }
  .skyline {
    position: absolute;
    top: 466px;
    left: 40px;
    width: 580px;
    height: 200px;
    background: linear-gradient(180deg, var(--skyline-light) 0%, var(--skyline-deep) 100%);
  }
  .volume-line {
    position: absolute;
    top: 708px;
    left: 0;
    width: 100%;
    text-align: center;
    font-family: "Oswald", sans-serif;
    font-weight: 500;
    font-size: 19px;
    letter-spacing: 3px;
    color: var(--ink-green);
  }
</style>
</head>
<body>
  <main class="label">
    <div class="label-frame"></div>
    <p class="distillery-name"><span>VALDENHOF</span><span>DESTILLERY</span></p>
    <h1 class="product-name">FELDMARER</h1>
    <p class="story">Seit 2015 produzieren wir mit Leidenschaft<br>Destillate, Liköre, Gin, Whisky<br>und kreative Kreationen. Genießen Sie die Passion<br>in jedem Tropfen.</p>
    <h2 class="product-type">GIN</h2>
    <div class="product-type-rule"></div>
    <div class="skyline" role="img" aria-label="Linienzeichnung einer Stadtsilhouette mit Pyramide, Kuppelbau und gotischer Kirche"></div>
    <p class="volume-line">40% ALC/VOL. 70CL/500 ML.</p>
  </main>
</body>
</html>
```